Need to design a business card with logo

Hellow
we are a company ,
PT REKA LINTAS MANDIRI
looking for design of name card.
what we do is property development and management.
design preferable professional corporate look and feel.
corporate. color, pantone colour 289
information required is
company name " Reka Lintas Mandiri"
person name eg " Peter Hollis"
person title eg "secret agent"
address: 9 kestrel road , jakarta, indonesia
phone : +6221 5906471
mobile : 0813 294 615
email : peter@hollistran.com
website: www.peterhol.com
if you want to include logo in the design you are welcome and appreciated , or you can simply use the company name as the logo.
thanks
corporate , business person , show events, exhibition events ,etc
Business

```html
<!DOCTYPE html>
<html lang="en">
<head>
<meta charset="utf-8">
<title>Reka Lintas Mandiri — Business Card</title>
<link href="https://fonts.googleapis.com/css2?family=Arimo:wght@700&family=Questrial&family=Raleway:wght@300&display=swap" rel="stylesheet">
<style>
  :root {
    --page-bg: #eceef0;
    --card-bg: #ffffff;
    --brand-navy: #1c3764;
    --brand-soft: #7e8fae;
    --text-grey: #5f6368;
    --icon-navy: #2c4778;
    --card-shadow: 0 10px 28px rgba(30, 40, 60, 0.16);
  }
  * { box-sizing: border-box; margin: 0; padding: 0; }
  html, body {
    width: 901px;
    height: 1200px;
    overflow: hidden;
    background: var(--page-bg);
  }
  .sheet {
    position: relative;
    width: 901px;
    height: 1200px;
  }
  .card {
    position: absolute;
    left: 100px;
    width: 700px;
    height: 400px;
    background: var(--card-bg);
    box-shadow: var(--card-shadow);
    overflow: hidden;
  }
  .card--contact { top: 150px; }
  .card--brand { top: 650px; }

  .wordmark {
    font-family: "Arimo", Arial, sans-serif;
    font-weight: 700;
    letter-spacing: -0.5px;
    white-space: nowrap;
  }
  .card--contact .wordmark {
    position: absolute;
    top: 70px;
    right: 70px;
    font-size: 34px;
    color: var(--brand-soft);
  }
  .card--brand .wordmark {
    position: absolute;
    top: 205px;
    left: 0;
    right: 0;
    text-align: center;
    font-size: 50px;
    color: var(--brand-navy);
  }

  .person {
    position: absolute;
    left: 56px;
    top: 180px;
    color: var(--text-grey);
  }
  .person__name {
    font-family: "Raleway", sans-serif;
    font-weight: 300;
    font-size: 26px;
    letter-spacing: 0.5px;
    text-transform: uppercase;
  }
  .person__title {
    font-family: "Questrial", sans-serif;
    font-size: 17px;
    margin-top: 2px;
    letter-spacing: 0.3px;
  }

  .contact-list {
    position: absolute;
    left: 56px;
    top: 250px;
    list-style: none;
    font-family: "Questrial", sans-serif;
    font-size: 16px;
    color: var(--text-grey);
  }
  .contact-list li {
    display: flex;
    align-items: center;
    gap: 10px;
    height: 24px;
  }
  .contact-list svg {
    width: 15px;
    height: 15px;
    flex: none;
    fill: none;
    stroke: var(--icon-navy);
    stroke-width: 1.8;
  }
  .contact-list svg .solid { fill: var(--icon-navy); stroke: none; }
</style>
</head>
<body>
<main class="sheet">

  <section class="card card--contact" aria-label="Business card, contact side">
    <div class="wordmark">Reka Lintas Mandiri</div>

    <div class="person">
      <p class="person__name">Peter Hollis</p>
      <p class="person__title">ultra-secret agent</p>
    </div>

    <ul class="contact-list">
      <li>
        <svg viewBox="0 0 16 16" aria-hidden="true"><path d="M8 15s5-5.2 5-8.6A5 5 0 0 0 3 6.4C3 9.8 8 15 8 15z"/><circle cx="8" cy="6.4" r="1.8"/></svg>
        <span>9 Kestrel Road , Jakarta, Indonesia</span>
      </li>
      <li>
        <svg viewBox="0 0 16 16" aria-hidden="true"><rect class="solid" x="2" y="5" width="12" height="10" rx="1"/><rect x="4" y="1.5" width="8" height="4"/></svg>
        <span>+6221 5906471</span>
      </li>
      <li>
        <svg viewBox="0 0 16 16" aria-hidden="true"><path class="solid" d="M4 1.5h3l1 3.5-2 1.2a8 8 0 0 0 3.8 3.8l1.2-2 3.5 1v3c0 1-1 2-2 2A11.5 11.5 0 0 1 2 3.5c0-1 1-2 2-2z"/></svg>
        <span>0813 294 615</span>
      </li>
      <li>
        <svg viewBox="0 0 16 16" aria-hidden="true"><rect x="1.5" y="3.5" width="13" height="9"/><path d="M1.5 3.5 8 9l6.5-5.5"/></svg>
        <span>peter@hollistran.com</span>
      </li>
      <li>
        <svg viewBox="0 0 16 16" aria-hidden="true"><rect x="2" y="2" width="12" height="12"/></svg>
        <span>www.peterhol.com</span>
      </li>
    </ul>
  </section>

  <section class="card card--brand" aria-label="Business card, brand side">
    <div class="wordmark">Reka Lintas Mandiri</div>
  </section>

</main>
</body>
</html>
```